Refresh of a Media Kit for Adtech Company - Needs jazzing up!

We have a Media Kit that's too ugly and boring to send to clients. Attaching some examples of ones we like better. Keep the general styling and theme of the current media kit (it's our brand style) and all the information conveyed, but please change anything and everything else to make it more dynamic. Attaching examples of media kits we like.

The "Media Kit Zarn" is the one you're designing, the others are just examples of media kits we liked.
Updates

Here's a link to "Glamour Shots" that can be used as appropriate throughout the Media kit: https://www.kelpvault.net/sh/k8pram21tzq0wnv/QQR7Lmxbeq5Tz_KP2rVbNdWHe?dl=0

Target Market(s)

Demand partners

Colors
0592cd
85cae6
34a7d8

Requirements
Nice to have
• Here are some glamour shots you can use if you see a good fit for any of them: https://www.kelpvault.net/sh/k8pram21tzq0wnv/QQR7Lmxbeq5Tz_KP2rVbNdWHe?dl=0

```html
<!DOCTYPE html>
<html lang="en">
<head>
<meta charset="utf-8">
<title>Zarn Media Kit 2021</title>
<link href="https://fonts.googleapis.com/css2?family=Roboto:wght@300;400;500;700&display=swap" rel="stylesheet">
<style>
  :root{
    --page:#e6e6e6;
    --blue:#1b8ef2;
    --blue-deep:#0592cd;
    --blue-soft:#85cae6;
    --blue-mid:#34a7d8;
    --ink:#2b2b2b;
    --muted:#555;
    --white:#fff;
  }
  *{margin:0;padding:0;box-sizing:border-box}
  html,body{width:1200px;height:724px;overflow:hidden;background:var(--page);font-family:'Roboto',sans-serif;color:var(--ink)}
  .canvas{position:relative;width:1200px;height:724px}
  .slide{position:absolute;width:544px;height:306px;background:var(--white);overflow:hidden}
  .slide > *{position:absolute}
  .s1{left:39px;top:40px;background:var(--blue)}
  .s2{left:617px;top:40px}
  .s3{left:39px;top:377px}
  .s4{left:617px;top:377px}
  .page-num{position:absolute;left:1164px;top:676px;font-size:36px;font-weight:300;color:#bdbdbd}

  .icon{width:30px;height:30px;border-radius:50%;background:var(--blue);display:flex;align-items:center;justify-content:center;transform:translate(-50%,-50%)}
  .icon svg{width:60%;height:60%}
  .icon.sm{width:25px;height:25px}
  .icon.lg{width:49px;height:49px}
  .caption{font-size:7px;line-height:9px;color:var(--muted);text-align:center;font-weight:300;transform:translateX(-50%);white-space:nowrap}
  .bar{height:2px;background:var(--blue-soft)}
  .rule{width:1px;background:#ddd}
  .footer{font-size:7px;letter-spacing:4.2px;color:var(--blue);top:292px;left:408px}
  .footer-brand{top:290px;left:493px;display:flex;align-items:center;gap:2px;font-size:7.5px;font-weight:500;color:var(--blue)}
  .footer-brand i{width:9px;height:9px;background:var(--blue);display:block;border-radius:1px}

  /* slide 1 */
  .s1 .brand{left:39px;top:42px;display:flex;align-items:center;gap:5px;font-size:17px;font-weight:500;color:var(--white)}
  .s1 .brand i{width:23px;height:23px;background:var(--white);border-radius:3px;display:block}
  .s1 .title{left:38px;top:102px;font-size:21px;line-height:26.5px;color:var(--white);font-weight:300}
  .s1 .title b{font-weight:700}
  .s1 .bar{left:39px;top:193px;width:78px;height:5px;background:var(--blue-soft);opacity:.8}
  .s1 .cta{left:39px;top:218px;width:93px;height:20px;background:#5fb2f6;color:var(--white);font-size:7.5px;font-weight:700;display:flex;align-items:center;justify-content:center;border-radius:2px}
  .s1 .contact{left:38px;top:250px;font-size:8.5px;color:#dfeeff;font-weight:300}
  .s1 .mosaic{left:265px;top:0;width:279px;height:306px;border-radius:60px 0 0 60px/150px 0 0 150px;background:linear-gradient(135deg,#3a4a5c,#7a8ea2 35%,#4b5a40 55%,#8a5a3a 75%,#2c3e55)}
  .s1 .kit{left:466px;top:290px;font-size:8.5px;color:var(--white);font-weight:300}

  /* slide 2 */
  .s2 .photo{left:0;top:0;width:168px;height:306px;border-radius:0 60px 60px 0/0 150px 150px 0;background:linear-gradient(160deg,#2f5fa0,#6b3a20 35%,#8a4a25 60%,#3c2415)}
  .s2 .headline{left:191px;top:27px;font-size:15.5px;line-height:20px;font-weight:300;width:340px}
  .s2 .headline b{font-weight:700}
  .s2 .colhead{font-size:11px;line-height:12.5px;font-weight:300}
  .s2 .colhead b{font-weight:700}

  /* slide 3 */
  .s3 .photo{left:263px;top:0;width:281px;height:306px;background:linear-gradient(90deg,rgba(255,255,255,1),rgba(190,180,150,.6) 30%,#7d7658 60%,#4c4632)}
  .s3 .head-box{left:0;top:24px;width:407px;height:51px;background:var(--white)}
  .s3 .headline{left:24px;top:26px;font-size:15.5px;line-height:20px;font-weight:300;white-space:nowrap}
  .s3 .headline b{font-weight:700}
  .s3 .colhead{top:92px;font-size:10px;font-weight:300}
  .s3 .colhead b{font-weight:700}
  .s3 .stat{font-size:7px;line-height:9px;color:var(--muted);font-weight:300}
  .s3 .stat b{color:var(--ink);font-weight:700;font-size:7.5px}
  .s3 .big{font-size:11px;font-weight:700;color:var(--ink)}
  .s3 .footer,.s3 .footer-brand{color:var(--white)}
  .s3 .footer-brand i{background:var(--white)}

  /* slide 4 */
  .s4 .headline{left:0;top:49px;width:544px;text-align:center;font-size:15.5px;line-height:20px;font-weight:300}
  .s4 .headline b{font-weight:700}
  .s4 .caption{font-size:9.5px;line-height:11px;color:#444;top:189px}
</style>
</head>
<body>
<svg width="0" height="0" style="position:absolute" aria-hidden="true">
  <defs>
    <symbol id="i-eye" viewBox="0 0 24 24"><g fill="none" stroke="#fff" stroke-width="1.6"><path d="M2 12s4-6 10-6 10 6 10 6-4 6-10 6S2 12 2 12z"/><circle cx="12" cy="12" r="3"/></g></symbol>
    <symbol id="i-coin" viewBox="0 0 24 24"><g fill="none" stroke="#fff" stroke-width="1.6"><circle cx="9" cy="9" r="5"/><path d="M9 6v6"/><circle cx="16" cy="16" r="4"/><path d="M14 16l1.5 1.5 3-3"/></g></symbol>
    <symbol id="i-person" viewBox="0 0 24 24"><g fill="none" stroke="#fff" stroke-width="1.6"><circle cx="11" cy="8" r="3"/><path d="M5 19c0-3 3-5 6-5s6 2 6 5"/><path d="M17 5l2 2-2 2"/></g></symbol>
    <symbol id="i-mega" viewBox="0 0 24 24"><g fill="none" stroke="#fff" stroke-width="1.6"><path d="M3 10v4h3l8 4V6L6 10H3z"/><path d="M17 9c1 1 1 5 0 6"/></g></symbol>
    <symbol id="i-play" viewBox="0 0 24 24"><g fill="none" stroke="#fff" stroke-width="1.6"><rect x="3" y="5" width="18" height="14" rx="2"/><path d="M3 9h18"/><path d="M10 12l4 2.5-4 2.5z"/></g></symbol>
    <symbol id="i-target" viewBox="0 0 24 24"><g fill="none" stroke="#fff" stroke-width="1.6"><circle cx="12" cy="12" r="8"/><circle cx="12" cy="12" r="4"/><path d="M12 12l7-7"/></g></symbol>
    <symbol id="i-refresh" viewBox="0 0 24 24"><g fill="none" stroke="#fff" stroke-width="1.6"><path d="M19 12a7 7 0 1 1-2-5"/><path d="M17 3v4h-4"/></g></symbol>
    <symbol id="i-walk" viewBox="0 0 24 24"><g fill="none" stroke="#fff" stroke-width="1.6" stroke-linecap="round"><circle cx="13" cy="4" r="2"/><path d="M11 8l-3 5M11 8l3 3 3 1M11 8l1 6-3 6M12 14l3 6"/></g></symbol>
    <symbol id="i-phone" viewBox="0 0 24 24"><g fill="none" stroke="#fff" stroke-width="1.6"><rect x="7" y="3" width="10" height="18" rx="2"/><path d="M11 18h2"/></g></symbol>
    <symbol id="i-percent" viewBox="0 0 24 24"><g fill="none" stroke="#fff" stroke-width="1.6"><path d="M6 18L18 6"/><circle cx="7" cy="7" r="2"/><circle cx="17" cy="17" r="2"/></g></symbol>
    <symbol id="i-pin" viewBox="0 0 24 24"><g fill="none" stroke="#fff" stroke-width="1.6"><path d="M12 21s-6-6-6-11a6 6 0 0 1 12 0c0 5-6 11-6 11z"/><circle cx="12" cy="10" r="2"/></g></symbol>
    <symbol id="i-hand" viewBox="0 0 24 24"><g fill="none" stroke="#fff" stroke-width="1.6"><circle cx="14" cy="8" r="4"/><path d="M3 18l4-3h5l3-2M3 21h9l6-4"/></g></symbol>
    <symbol id="i-swipe" viewBox="0 0 24 24"><g fill="none" stroke="#fff" stroke-width="1.6"><rect x="6" y="3" width="11" height="14" rx="1"/><path d="M9 21l2-6 5 2M4 8l2-2 2 2"/></g></symbol>
    <symbol id="i-chart" viewBox="0 0 24 24"><g fill="none" stroke="#fff" stroke-width="1.6"><path d="M4 20h16M7 20v-5M11 20v-8M15 20v-6M19 20v-10"/><path d="M5 11l5-5 4 3 6-6"/></g></symbol>
  </defs>
</svg>

<main class="canvas">
  <section class="slide s1">
    <div class="brand"><i></i>Zarn</div>
    <h1 class="title">Zarn<br>Your <b>Pathway</b> to<br>Programmatic DOOH</h1>
    <div class="bar"></div>
    <div class="cta">BUY ON ZARN</div>
    <p class="contact">hello@zarnmedia.net &nbsp;1-555-014-2288</p>
    <div class="mosaic" role="img" aria-label="Wall of many screens showing varied travel, nature and city photographs"></div>
    <p class="kit">MEDIA KIT 2021</p>
  </section>

  <section class="slide s2">
    <div class="photo" role="img" aria-label="Pub interior with wooden bar and mounted digital screens"></div>
    <h2 class="headline">DOOH is the <b>“now”</b> frontier of digital advertising, and your advertisers will soon be demanding it, if they aren’t already.</h2>
    <p class="colhead" style="left:200px;top:104px"><b>Consumers</b> are ready to leave<br>their homes and spend</p>
    <div class="bar" style="left:200px;top:131px;width:56px"></div>
    <p class="colhead" style="left:357px;top:102px"><b>Brands</b> are ready to<br>follow their consumers</p>
    <div class="bar" style="left:357px;top:129px;width:56px"></div>
    <div class="rule" style="left:349px;top:103px;height:173px"></div>

    <div class="icon" style="left:237px;top:159px"><svg><use href="#i-walk"/></svg></div>
    <p class="caption" style="left:237px;top:181px">Walking/driving<br>behavior way up</p>
    <div class="icon" style="left:306px;top:159px"><svg><use href="#i-phone"/></svg></div>
    <p class="caption" style="left:306px;top:181px">Screen fatigue,<br>changing data privacy<br>landscape driving<br>budgets away from<br>mobile/display</p>
    <div class="icon" style="left:239px;top:219px"><svg><use href="#i-pin"/></svg></div>
    <p class="caption" style="left:239px;top:241px">Consumers plan to<br>spend 25% of their<br>lockdown-induced<br>savings this summer</p>
    <div class="icon" style="left:406px;top:159px"><svg><use href="#i-percent"/></svg></div>
    <p class="caption" style="left:406px;top:181px"><b>60%</b> increase in DOOH<br>spending in 2021</p>
    <div class="icon" style="left:406px;top:219px"><svg><use href="#i-hand"/></svg></div>
    <p class="caption" style="left:406px;top:241px"><b>3B$</b> projected 2021 DOOH<br>spend in the U.S. alone.</p>

    <p class="footer">DOOH NOW</p>
    <div class="footer-brand"><i></i>Zarn</div>
  </section>

  <section class="slide s3">
    <div class="photo" role="img" aria-label="Waiting room with a woman using her phone beside a wall-mounted ad screen"></div>
    <div class="head-box"></div>
    <h2 class="headline">But it’s not just lockdowns ending - this <b>uptick</b> has been<br>driven by the unique effectiveness of DOOH ad exposure.</h2>

    <p class="colhead" style="left:33px">It’s <b>special...</b></p>
    <div class="bar" style="left:34px;top:107px;width:36px"></div>
    <p class="colhead" style="left:168px">It’s <b>powerful</b></p>
    <div class="bar" style="left:169px;top:107px;width:36px"></div>
    <p class="colhead" style="left:251px">And it <b>works</b></p>
    <div class="bar" style="left:252px;top:107px;width:28px"></div>
    <div class="rule" style="left:159px;top:90px;height:163px"></div>
    <div class="rule" style="left:244px;top:90px;height:163px"></div>

    <div class="icon sm" style="left:63px;top:131px"><svg><use href="#i-eye"/></svg></div>
    <p class="caption" style="left:63px;top:147px">Forced dwell<br>time</p>
    <div class="icon sm" style="left:126px;top:131px"><svg><use href="#i-coin"/></svg></div>
    <p class="caption" style="left:126px;top:147px">Brand-safe →<br>brand loyal</p>
    <div class="icon sm" style="left:63px;top:183px"><svg><use href="#i-person"/></svg></div>
    <p class="caption" style="left:63px;top:200px">100% viewability<br>by humans,<br>not bots</p>
    <div class="icon sm" style="left:126px;top:183px"><svg><use href="#i-mega"/></svg></div>
    <p class="caption" style="left:126px;top:200px">Lends well to<br>creative<br>messaging</p>
    <div class="icon sm" style="left:63px;top:245px"><svg><use href="#i-play"/></svg></div>
    <p class="caption" style="left:63px;top:262px">Not Skippable</p>

    <div class="icon sm" style="left:182px;top:131px"><svg><use href="#i-target"/></svg></div>
    <p class="stat" style="left:170px;top:147px">Vs. traditional OOH,</p>
    <p class="stat" style="left:170px;top:165px"><b>DOOH 2x</b><br>more likely to be<br>seen, recalled,</p>
    <p class="big" style="left:170px;top:198px">2.5x</p>
    <p class="stat" style="left:170px;top:213px">more impactful.</p>

    <div class="icon sm" style="left:265px;top:131px"><svg><use href="#i-refresh"/></svg></div>
    <p class="big" style="left:256px;top:164px">~100%</p>
    <p class="stat" style="left:256px;top:180px">increase in reach if<br>added to “OMNI-<br>Channel”<br>campaigns</p>

    <p class="footer">DOOH NOW</p>
    <div class="footer-brand"><i></i>Zarn</div>
  </section>

  <section class="slide s4">
    <h2 class="headline">Despite this exploding interest in <b>DOOH</b>, several crucial issues<br>persist for players trying to make use of this channel.</h2>
    <div class="icon lg" style="left:151px;top:149px"><svg><use href="#i-coin"/></svg></div>
    <p class="caption" style="left:151px">Premium pricing on the<br>largest publisher networks<br>makes adding this channel<br>cost-prohibitive</p>
    <div class="icon lg" style="left:272px;top:149px"><svg><use href="#i-swipe"/></svg></div>
    <p class="caption" style="left:272px">Medium-sized publisher<br>networks either force<br>advertisers to use their in-<br>house DSP, or favor<br>clients who use said DSP</p>
    <div class="icon lg" style="left:393px;top:149px"><svg><use href="#i-chart"/></svg></div>
    <p class="caption" style="left:393px">Rare to find screen<br>networks with even basic<br>analytics, optimization<br>capabilities</p>
    <p class="footer">DOOH NOW</p>
    <div class="footer-brand"><i></i>Zarn</div>
  </section>

  <p class="page-num">1</p>
</main>
</body>
</html>
```